Fallowmere community hall home page

We are building a modern, responsive website & booking system for our community hall. For this SketchHarbor task, we would like to receive design ideas for the home page.
There are no limits on the colours or fonts that can be used. We are looking for a modern, fresh design with a local/community feel. We don’t have a logo but we also recognise that our name is quite long! … So initials (Fallowmere) instead of the name would be fine.
People book our community hall for a range of activities including: fitness classes, wedding receptions, birthday parties, business meetings, teaching, community events, charity fundraisers and other celebrations.
We have three main goals for the website. The first is that people can check our calendar and make a booking for an available time slot. The second is that they can read about our facilities and the prices for hiring them. The third is that people can find out about upcoming activities & events.
CTA: Book now
A button that links to a booking request form. (The form is not part of this design project)
Primary/Header navigation:
Home | Calendar | Facilities | Prices | Photos | News | Contact
Secondary/Footer navigation:
Chatterbook | Quipper
Login | Register | Privacy policy | Terms & conditions
Example texts (lorem ipsum etc. is also fine):
We have everything you need from a venue, whether it’s an elegant room with ample flexible space, a lavish and elegant hall for a wedding reception, a conference room that fits 125 delegates or a easy access venue to the town centre.
The hall is available for hire for wedding receptions, birthday celebrations, anniversaries, children's parties, presentations, lectures, fitness groups, and will comfortably accommodate all your guests.
This venue is well equipped with a modern kitchen, a range of audio and technical services, hearing loop, licensed bar, conference facilities, disabled access and unlimited free WiFi.
You can use this website to find out more about our rooms, equipment and the services we can offer and use the calendar to see where we have rooms available. You can also book rooms using our online booking system.
To the front of the building is a large public open grassed area across which is a row of shops. To the rear of the building is the large car park, including spaces for blue badge holders and a large enclosed cycle rack. This area also has extensive gardens, with seating and planting areas maintained by local volunteers.
The community hall is run and managed by volunteers of the Fallowmere Community Organisation. Our objectives are to increase opportunities for people living in and around Fallowmere.
We are passionate about being the heart of the community; caring for this community centred property and visitors are at the heart of all we do.
Where to go next
— Check when the hall is free
— Read our booking policy documents
— Make a booking reservation
Amenities
— Free WiFi
— Free car parking
— Fully equipped kitchen
— Hearing loop
Details for our most popular facilities (rooms):
Name: Main hall
Short description: A 127 square metre main hall with entrance lobby, toilets, a well-equipped kitchen and separate storage facilities. Three sets of double doors provide access to a large paved area and the adjacent playing field.
Capacity: 180 people
Price: £10-20 per hour
Links: More info | Book now
Name: Large meeting room
Short description: A delightful, spacious room with an outlook and access to the small walled garden. Ideal for meetings and small gatherings - it has its own access door and the use of a disabled W/C. We offer a reduced rate for this room when booked together with the main hall.
Capacity: 20 people
Price: £6-12 per hour
Attachments:
We have attached some photos of the hall & some (royalty free) stock images for inspiration.

```html
<!DOCTYPE html>
<html lang="en">
<head>
<meta charset="utf-8">
<title>Fallowmere Community Hall</title>
<link href="https://fonts.googleapis.com/css2?family=Roboto:wght@400;500;700;900&family=Open+Sans:wght@400;600&display=swap" rel="stylesheet">
<style>
:root{
  --accent:#e8461e;
  --ink:#1d1d1d;
  --text:#3a3a3a;
  --muted:#6b6b6b;
  --soft:#f3f0f1;
  --white:#ffffff;
  --footer:#262626;
  --line:#b9b9b9;
  --head:"Roboto",Arial,sans-serif;
  --body:"Open Sans",Arial,sans-serif;
}
*{box-sizing:border-box;margin:0;padding:0}
html,body{width:1200px;height:4211px;overflow:hidden}
body{font-family:var(--body);color:var(--text);background:var(--white);position:relative}
a{text-decoration:none}
section,footer{position:absolute;left:0;width:1200px}
.abs{position:absolute}
.btn{position:absolute;display:flex;align-items:center;justify-content:center;background:var(--accent);color:var(--white);font-family:var(--head);font-weight:700;border-radius:30px;text-transform:uppercase;letter-spacing:.3px;text-decoration:none}
.btn-ghost{background:var(--white);color:var(--accent);border:2px solid var(--accent)}
.section-title{position:absolute;font-family:var(--head);font-weight:700;color:var(--ink);text-transform:uppercase;font-size:23px;letter-spacing:.2px}
.rule{position:absolute;height:2px;background:var(--line);width:44px}

/* brand name */
.brand{position:absolute;display:flex;align-items:center;gap:10px;font-family:var(--head);font-weight:500;color:var(--white);text-transform:uppercase;letter-spacing:2px}
.brand i{display:block;background:var(--white)}
.hero .brand{left:128px;top:33px;font-size:20px}
.hero .brand i{width:12px;height:12px}

/* hero */
.hero{top:0;height:700px;background:linear-gradient(180deg,#3b1f4e 0%,#4a2a5a 25%,#3a2d3a 55%,#2a2227 100%)}
.hero-photo{position:absolute;inset:0;background:radial-gradient(ellipse at 70% 25%,rgba(200,90,150,.35),transparent 45%),radial-gradient(ellipse at 20% 30%,rgba(120,60,200,.45),transparent 40%),linear-gradient(180deg,rgba(0,0,0,.1),rgba(0,0,0,.45))}
.main-nav{position:absolute;right:134px;top:36px;display:flex;gap:29px}
.main-nav a{color:var(--white);font-family:var(--head);font-weight:500;font-size:13px}
.hero-title{position:absolute;left:0;width:1200px;top:188px;text-align:center;font-family:var(--head);font-weight:900;font-size:35px;color:var(--white);text-transform:uppercase}
.hero .btn{left:518px;top:256px;width:164px;height:49px;font-size:18px}
.dots{position:absolute;left:563px;top:653px;display:flex;gap:9px}
.dots span{width:7px;height:7px;border-radius:50%;background:var(--white)}
.dots span.on{background:var(--accent)}

/* welcome */
.welcome{top:700px;height:516px}
.pic{position:absolute}
.welcome .pic-hall{left:131px;top:54px;width:397px;height:371px;background:linear-gradient(160deg,#efe6cf,#c9b48a 45%,#39406a 100%);border-radius:4px}
.welcome .pic-flowers{left:335px;top:178px;width:281px;height:283px;background:linear-gradient(150deg,#6a6a58,#e6a47a 45%,#d9d4cc 100%);border:6px solid var(--white);border-radius:6px}
.eyebrow{left:664px;top:62px;font-family:var(--head);font-size:17px;color:var(--ink)}
.welcome h1{position:absolute;left:664px;top:88px;font-family:var(--head);font-weight:700;font-size:25px;color:var(--ink)}
.welcome .rule{left:664px;top:139px;width:121px}
.welcome p{position:absolute;left:665px;top:172px;width:400px;font-size:15px;line-height:24px;color:var(--text)}
.welcome .btn{left:669px;top:417px;width:103px;height:31px;font-size:11px}

/* upcoming */
.upcoming{top:1216px;height:551px;background:var(--soft)}
.upcoming .section-title{left:131px;top:40px}
.upcoming .rule{left:131px;top:76px;width:68px}
.arrows{position:absolute;left:688px;top:56px;display:flex;gap:14px}
.card{position:absolute;background:var(--white);border-radius:4px;overflow:hidden}
.event{top:107px;width:297px;height:390px}
.event .pic{left:0;top:0;width:297px;height:178px}
.event h3{position:absolute;left:29px;top:203px;width:240px;font-family:var(--head);font-weight:500;font-size:13px;line-height:20px;color:var(--ink);text-transform:uppercase}
.event p{position:absolute;left:29px;top:261px;width:240px;font-size:12px;line-height:19px}
.event .btn{left:29px;top:333px;width:91px;height:26px;font-size:10px}
.calendar{left:765px;top:107px;width:298px;height:390px}
.cal-head{position:absolute;left:0;top:18px;width:298px;text-align:center;font-family:var(--head);font-weight:500;font-size:13px;color:var(--ink)}
.cal-prev,.cal-next{position:absolute;top:20px}
.cal-prev{left:28px}.cal-next{right:28px}
.cal-grid{position:absolute;left:10px;top:62px;width:278px;display:grid;grid-template-columns:repeat(7,1fr)}
.cal-grid .dow{height:30px;background:#eeeeee;display:flex;align-items:center;justify-content:center;font-family:var(--head);font-weight:700;font-size:11px;color:var(--ink)}
.cal-grid .day{height:42px;display:flex;flex-direction:column;align-items:center;justify-content:center;font-size:11px;color:var(--ink);gap:4px}
.cal-grid .day.shade{background:#f4f4f4}
.cal-grid .day i{width:4px;height:4px;background:var(--accent)}
.cal-grid .day i.y{background:#f2b01e}
.cal-info{position:absolute;left:26px;top:288px;width:250px}
.cal-info .when{font-family:var(--head);font-size:12px;color:var(--ink)}
.cal-info h4{font-family:var(--head);font-weight:500;font-size:13px;color:var(--ink);margin-top:8px}
.cal-info p{font-size:11px;line-height:17px;margin-top:8px}

/* amenities */
.amenities{top:1767px;height:502px;background:radial-gradient(ellipse at 55% 30%,#5b4a3a,#2b2520 55%,#16130f 100%)}
.amenities .section-title{left:0;width:1200px;text-align:center;top:50px;color:var(--white);font-size:22px}
.amenities .rule{left:578px;top:92px;background:#e7d7c6}
.amenity{position:absolute;top:340px;width:260px;text-align:center;color:var(--white)}
.amenity svg{display:block;margin:0 auto 14px}
.amenity span{font-family:var(--head);font-weight:700;font-size:17px;text-transform:uppercase}

/* photos */
.photos{top:2269px;height:805px}
.photos .section-title{left:0;width:1200px;text-align:center;top:46px}
.photos .rule{left:578px;top:84px}
.tile{position:absolute;width:297px;height:298px;border-radius:4px;display:flex;align-items:center;justify-content:center;text-align:center;font-family:var(--head);font-weight:900;font-size:22px;line-height:29px;color:var(--white);text-transform:uppercase}
.r1{top:126px}.r2{top:445px}
.c1{left:131px}.c2{left:450px}.c3{left:768px}

/* facilities */
.facilities{top:3074px;height:781px;background:var(--soft)}
.facilities .section-title{left:0;width:1200px;text-align:center;top:46px}
.facilities .rule{left:578px;top:87px}
.room{top:132px;width:456px;height:600px}
.room .pic{left:0;top:0;width:456px;height:291px}
.room h3{position:absolute;left:38px;top:320px;font-family:var(--head);font-weight:700;font-size:17px;color:var(--ink);text-transform:uppercase}
.room p{position:absolute;left:38px;top:352px;width:390px;font-size:13.5px;line-height:20.5px}
.room .specs{position:absolute;left:38px;top:466px;display:flex}
.spec{font-size:13.5px;color:var(--text)}
.spec b{display:block;font-family:var(--head);font-weight:500;font-size:17px;color:var(--ink);margin-top:4px}
.spec.cap{border-left:1px solid #bdbdbd;padding-left:38px}
.room .btn{top:552px;height:31px;font-size:11px}

/* footer */
.site-footer{top:3855px;height:356px;background:var(--footer);color:var(--white)}
.site-footer .brand{left:131px;top:118px;font-size:24px}
.site-footer .brand i{width:14px;height:14px}
.f-col{position:absolute;top:59px}
.f-col h5{font-family:var(--head);font-weight:700;font-size:12px;letter-spacing:.3px;margin-bottom:16px}
.f-menu{left:399px}
.f-menu a{display:block;color:#dcdcdc;font-size:11px;line-height:20px;text-transform:uppercase}
.f-contact{left:610px}
.f-follow{left:955px}
.f-item{display:flex;align-items:flex-start;gap:10px;margin-bottom:16px;font-size:11px;line-height:15px;color:#dcdcdc}
.f-item .dot{flex:none;width:22px;height:22px;border-radius:50%;background:var(--white);display:flex;align-items:center;justify-content:center;margin-top:2px}
.f-bottom{position:absolute;left:131px;right:134px;top:268px;border-top:1px solid #444}
.f-bottom .links{position:absolute;left:3px;top:43px;font-size:10.5px;color:#dcdcdc}
.f-bottom .copy{position:absolute;right:0;top:43px;font-size:10.5px;color:#dcdcdc}
</style>
</head>
<body>

<section class="hero">
  <div class="hero-photo" role="img" aria-label="Guests seated at round tables in a hall lit with purple light and stained-glass windows"></div>
  <div class="brand"><i></i>Fallowmere</div>
  <nav class="main-nav">
    <a href="#">HOME</a><a href="#">CALENDAR</a><a href="#">FACILITIES</a><a href="#">PRICES</a><a href="#">PHOTOS</a><a href="#">NEWS</a><a href="#">CONTACT</a>
  </nav>
  <h2 class="hero-title">Wedding Reception Halls</h2>
  <a class="btn" href="#">Book now</a>
  <div class="dots"><span></span><span></span><span class="on"></span><span></span><span></span></div>
</section>

<section class="welcome">
  <div class="pic pic-hall" role="img" aria-label="Hall laid out with round tables and blue chairs under a chandelier"></div>
  <div class="pic pic-flowers" role="img" aria-label="Table flower arrangement with a place card"></div>
  <div class="abs eyebrow">WELCOME TO</div>
  <h1>FALLOWMERE COMMUNITY HALL</h1>
  <div class="rule"></div>
  <p>Lorem Ipsum is simply dummy text of the printing and typesetting industry. Lorem Ipsum has been the industry's standard dummy text ever since the 1500s, when an unknown printer took a galley of type and scrambled it to make a type specimen book. It has survived not only five centuries, but also the leap into electronic typesetting, remaining essentially un changed. It was popularised in the.</p>
  <a class="btn" href="#">Read more</a>
</section>

<section class="upcoming">
  <h2 class="section-title">Upcoming activities</h2>
  <div class="rule"></div>
  <div class="arrows">
    <svg width="18" height="22" viewBox="0 0 18 22"><path d="M13 2 4 11l9 9" fill="none" stroke="#555" stroke-width="2.4"/></svg>
    <svg width="18" height="22" viewBox="0 0 18 22"><path d="M5 2l9 9-9 9" fill="none" stroke="#555" stroke-width="2.4"/></svg>
  </div>

  <article class="card event" style="left:131px">
    <div class="pic" role="img" aria-label="Person sitting cross-legged in a yoga class" style="background:linear-gradient(135deg,#f1ece6,#d8c7b6 55%,#9a8b7c)"></div>
    <h3>Lorem ipsum is simply dummy text of the printing</h3>
    <p>Lorem Ipsum is simply dummy text of the printing and types etting industry. Lorem Ipsum has been.</p>
    <a class="btn" href="#">Read more</a>
  </article>

  <article class="card event" style="left:445px">
    <div class="pic" role="img" aria-label="Candle centrepiece on a table under purple light" style="background:radial-gradient(circle at 50% 60%,#f0a030,#8a2a6a 35%,#3a1050 80%)"></div>
    <h3>Lorem ipsum is simply dummy text of the printing</h3>
    <p>Lorem Ipsum is simply dummy text of the printing and types etting industry. Lorem Ipsum has been.</p>
    <a class="btn" href="#">Read more</a>
  </article>

  <article class="card calendar">
    <svg class="cal-prev" width="10" height="12" viewBox="0 0 10 12"><path d="M7 1 2 6l5 5" fill="none" stroke="#333" stroke-width="1.6"/></svg>
    <div class="cal-head">FEBRUARY, 2021</div>
    <svg class="cal-next" width="10" height="12" viewBox="0 0 10 12"><path d="M3 1l5 5-5 5" fill="none" stroke="#333" stroke-width="1.6"/></svg>
    <div class="cal-grid">
      <div class="dow">MO</div><div class="dow">TU</div><div class="dow">WE</div><div class="dow">TH</div><div class="dow">FR</div><div class="dow">SA</div><div class="dow">SU</div>
      <div class="day">01<i></i></div><div class="day">02<i></i></div><div class="day">03<i></i></div><div class="day">04<i></i></div><div class="day">05<i></i></div><div class="day">06<i class="y"></i></div><div class="day">07<i></i></div>
      <div class="day shade">08<i class="y"></i></div><div class="day shade">09<i></i></div><div class="day shade">10<i></i></div><div class="day shade">11<i></i></div><div class="day shade">12<i></i></div><div class="day shade">13<i></i></div><div class="day shade">14<i class="y"></i></div>
      <div class="day">15<i></i></div><div class="day">16<i></i></div><div class="day">17<i></i></div><div class="day">18<i></i></div><div class="day">19<i></i></div><div class="day">20<i class="y"></i></div><div class="day">21<i></i></div>
      <div class="day shade">22<i></i></div><div class="day shade">23<i class="y"></i></div><div class="day shade">24<i></i></div><div class="day shade">25<i class="y"></i></div><div class="day shade">26<i></i></div><div class="day shade">27<i></i></div><div class="day shade">28<i class="y"></i></div>
    </div>
    <div class="cal-info">
      <div class="when">FEB 10,2021 &nbsp;|&nbsp; 10:00 AM</div>
      <h4>LOREM IPSUM IS SIMPLY</h4>
      <p>Lorem Ipsum is simply dummy text of the printing going to use a passage of Lore.</p>
    </div>
  </article>
</section>

<section class="amenities" role="img" aria-label="Candle holders on a dimly lit banquet table">
  <h2 class="section-title">Amenities</h2>
  <div class="rule"></div>

  <div class="amenity" style="left:96px">
    <svg width="62" height="48" viewBox="0 0 62 48" fill="none" stroke="#fff" stroke-width="6" stroke-linecap="round"><path d="M5 17a37 37 0 0 1 52 0"/><path d="M15 27a23 23 0 0 1 32 0"/><circle cx="31" cy="40" r="4" fill="#fff" stroke="none"/></svg>
    <span>Free WiFi</span>
  </div>
  <div class="amenity" style="left:311px">
    <svg width="62" height="56" viewBox="0 0 62 56" fill="none" stroke="#fff" stroke-width="2.4"><rect x="8" y="2" width="22" height="22" rx="2"/><path d="M16 19V8h5a4 4 0 0 1 0 8h-5"/><path d="M4 46v-8l6-10h32l10 10h6v8z"/><circle cx="16" cy="47" r="5" fill="#262626"/><circle cx="46" cy="47" r="5" fill="#262626"/></svg>
    <span>Free car parking</span>
  </div>
  <div class="amenity" style="left:576px">
    <svg width="62" height="56" viewBox="0 0 62 56" fill="none" stroke="#fff" stroke-width="2.2"><path d="M8 10h46M14 4h34"/><rect x="4" y="20" width="54" height="34"/><rect x="10" y="28" width="18" height="20"/><path d="M36 28h16M36 36h16M36 44h16M10 20v-6h14v6"/></svg>
    <span>Fully equipped kitchen</span>
  </div>
  <div class="amenity" style="left:825px">
    <svg width="62" height="56" viewBox="0 0 62 56" fill="none" stroke="#fff" stroke-width="2.6" stroke-linecap="round"><path d="M26 18a14 14 0 1 1 26 8c-3 4-7 6-7 12a8 8 0 0 1-14 4"/><path d="M32 20a8 8 0 0 1 14 2c0 4-4 5-4 9"/><path d="M16 20a10 10 0 0 0 0 14M10 16a16 16 0 0 0 0 22"/></svg>
    <span>Hearing loop</span>
  </div>
</section>

<section class="photos">
  <h2 class="section-title">Photos</h2>
  <div class="rule"></div>
  <div class="tile r1 c1" role="img" aria-label="Person kneeling on a blue exercise mat" style="background:linear-gradient(180deg,#a99682 0%,#7c6a5c 45%,#2f6da3 70%,#a08468 100%)">Fitness classes</div>
  <div class="tile r1 c2" role="img" aria-label="Banquet room laid for a wedding reception" style="background:linear-gradient(160deg,#8c7c66,#5e4d3e 50%,#b6a88f)">Wedding<br>receptions</div>
  <div class="tile r1 c3" role="img" aria-label="Party table with cakes and treats" style="background:linear-gradient(160deg,#9fbf9a,#c79aa6 50%,#7aa6c2)">Birthday<br>parties</div>
  <div class="tile r2 c1" role="img" aria-label="Meeting room with long table and projector screen" style="background:linear-gradient(180deg,#b4b2a6,#7d7a70 50%,#4f4337)">Business meetings</div>
  <div class="tile r2 c2" role="img" aria-label="Hall with tall stained-glass windows" style="background:linear-gradient(180deg,#a6603a,#7c4a6c 45%,#2e4a7a 85%,#cfd3e2)">Community<br>events</div>
  <div class="tile r2 c3" role="img" aria-label="Crowd at a celebration under coloured lights" style="background:linear-gradient(180deg,#2e3a5e,#3a2a48 55%,#1c1a24)">Other<br>celebrations</div>
</section>

<section class="facilities">
  <h2 class="section-title">Our most popular facilities</h2>
  <div class="rule"></div>

  <article class="card room" style="left:131px">
    <div class="pic" role="img" aria-label="Main hall with tiered seating" style="background:linear-gradient(180deg,#5a5a5c,#3a3f48 50%,#2a2c34)"></div>
    <h3>Main hall</h3>
    <p>A 127 square metre main hall with entrance lobby, toilets, a well-equipped kitchen and separate storage facilities. Three sets of double doors provide access to a large paved area and the adjacent playing field.</p>
    <div class="specs">
      <div class="spec" style="width:175px">Price:<b>£10-20 per hour</b></div>
      <div class="spec cap">Capacity:<b>180 people</b></div>
    </div>
    <a class="btn" href="#" style="left:38px;width:102px">Book now</a>
    <a class="btn btn-ghost" href="#" style="left:150px;width:101px">More info</a>
  </article>

  <article class="card room" style="left:610px">
    <div class="pic" role="img" aria-label="Large meeting room with long table and projector screen" style="background:linear-gradient(180deg,#c9cbc6,#8e8c82 50%,#5a4636)"></div>
    <h3>Large meeting room</h3>
    <p>A delightful, spacious room with an outlook and access to the small walled garden. Ideal for meetings and small gatherings - it has its own access door and the use of a disabled W/C. We offer a reduced rate for this room when booked together with the main hall.</p>
    <div class="specs">
      <div class="spec" style="width:175px">Price:<b>£6-12 per hour</b></div>
      <div class="spec cap">Capacity:<b>20 people</b></div>
    </div>
    <a class="btn" href="#" style="left:38px;width:102px">Book now</a>
    <a class="btn btn-ghost" href="#" style="left:150px;width:101px">More info</a>
  </article>
</section>

<footer class="site-footer">
  <div class="brand"><i></i>Fallowmere</div>

  <div class="f-col f-menu">
    <h5>MENU</h5>
    <a href="#">Home</a><a href="#">Calendar</a><a href="#">Facilities</a><a href="#">Prices</a><a href="#">Photos</a><a href="#">News</a><a href="#">Contact</a>
  </div>

  <div class="f-col f-contact">
    <h5>CONTACT US</h5>
    <div class="f-item"><span class="dot"><svg width="10" height="12" viewBox="0 0 10 12"><path d="M5 11S1 6.5 1 4a4 4 0 0 1 8 0c0 2.5-4 7-4 7z" fill="#262626"/><circle cx="5" cy="4" r="1.4" fill="#fff"/></svg></span><span>27 Orchard Row<br>Fallowmere, FM4 2LD</span></div>
    <div class="f-item"><span class="dot"><svg width="11" height="11" viewBox="0 0 11 11"><path d="M2 1l2 2-1 1.5a6 6 0 0 0 3.5 3.5L8 7l2 2-1.5 1.5C4.5 10 1 6.5.5 2.5z" fill="#262626"/></svg></span><span>Call Us<br>01632 960 418</span></div>
    <div class="f-item"><span class="dot"><svg width="11" height="9" viewBox="0 0 11 9"><rect x=".5" y=".5" width="10" height="8" fill="#262626"/><path d="M.5.5 5.5 5l5-4.5" fill="none" stroke="#fff"/></svg></span><span>E mail Us<br>info@FallowmereCommunityHall.com</span></div>
  </div>

  <div class="f-col f-follow">
    <h5>FOLLOW US</h5>
    <div class="f-item"><span class="dot"></span><span>Like us on<br>CHATTERBOOK</span></div>
    <div class="f-item"><span class="dot"></span><span>Follow us on<br>QUIPPER</span></div>
    <div class="f-item"><span class="dot"></span><span>Follow us on<br>LINKHAVEN</span></div>
  </div>

  <div class="f-bottom">
    <div class="links">LOGIN | REGISTER | PRIVACY POLICY | TERMS &amp; CONDITIONS</div>
    <div class="copy">Copyright © 2021 All Rights Reserved</div>
  </div>
</footer>

</body>
</html>
```